Residential Construction Business - Site Signage

I need a design made for a site fence banner. We have a logo and branding so the design would need to be aligned with this. It would need to be made to specific size ratio so that it can be sent to the maker for production.
ratio : 4600 wide x 1700 high
The design should feature our website and also the slogan
"don't move, re-imagine"

Target Market(s)

potential clients

Industry/Entity Type

construction

Font styles to use
Other font styles liked:
• to match branding

Colors
0054AA
0677BA
7BADD7
CADEEF
E8F1F8

Requirements
Must have
• www.velmbuild.com.au Majority of the sign is our brand logo
Nice to have
• Majority of the sign is our brand logo
Should not have
• colors and themes that arent brand relevant

```html
<!DOCTYPE html>
<html lang="en">
<head>
<meta charset="utf-8">
<title>Velm Build – Site Fence Banner</title>
<link rel="stylesheet" href="https://fonts.googleapis.com/css2?family=Montserrat:wght@600&family=Roboto+Condensed:wght@400;700&display=swap">
<style>
  :root {
    --stage: #959ca4;
    --navy: #043a5e;
    --navy-deep: #032d4a;
    --tag-blue: #0c5e93;
    --white: #ffffff;
    --headline-grey: #e2e2e2;
    --web-band: #e4e4e4;
    --ink: #111111;
    --tag-text: #d4e4f1;
  }
  * { margin: 0; padding: 0; box-sizing: border-box; }
  html, body {
    width: 1093px;
    height: 1200px;
    overflow: hidden;
    background: var(--stage);
  }
  .banner {
    position: absolute;
    left: 46px;
    top: 415px;
    width: 1000px;
    height: 370px;
    background: var(--navy);
    box-shadow: 0 10px 24px rgba(0, 0, 0, 0.35);
    overflow: hidden;
  }
  .banner-shapes {
    position: absolute;
    inset: 0;
  }
  .brand-name {
    position: absolute;
    left: 60px;
    top: 170px;
    font-family: "Montserrat", sans-serif;
    font-weight: 600;
    font-size: 27px;
    letter-spacing: 0.3em;
    color: var(--navy);
    line-height: 1;
    white-space: nowrap;
  }
  .slogan {
    position: absolute;
    left: 538px;
    top: 46px;
    font-family: "Roboto Condensed", sans-serif;
    line-height: 1;
    white-space: nowrap;
  }
  .slogan-line {
    display: block;
    font-size: 82px;
  }
  .slogan-line--strong {
    font-weight: 700;
    color: var(--headline-grey);
  }
  .slogan-line--light {
    font-weight: 400;
    color: var(--white);
    letter-spacing: 0.02em;
    margin-top: -12px;
  }
  .services {
    position: absolute;
    top: 203px;
    left: 541px;
    display: flex;
    gap: 5px;
    list-style: none;
  }
  .service {
    height: 18px;
    padding: 0 7px;
    display: flex;
    align-items: center;
    font-family: "Montserrat", sans-serif;
    font-weight: 600;
    font-size: 12px;
    letter-spacing: 0.13em;
    color: var(--tag-text);
    background: var(--tag-blue);
  }
  .service--dark { background: var(--navy-deep); }
  .website {
    position: absolute;
    right: 46px;
    top: 274px;
    font-family: "Roboto Condensed", sans-serif;
    font-weight: 700;
    font-size: 46px;
    line-height: 1.2;
    color: var(--ink);
    white-space: nowrap;
  }
</style>
</head>
<body>
  <section class="banner" aria-label="Velm Build site fence banner">
    <svg class="banner-shapes" viewBox="0 0 1000 370" width="1000" height="370" aria-hidden="true">
      <path class="brand-panel" fill="var(--white)"
            d="M0 0 H347 L503 164 Q513 183 503 202 L347 370 H0 Z"/>
      <polygon class="web-band" fill="var(--web-band)"
               points="455,270 1000,270 1000,332 400,332"/>
    </svg>

    <p class="brand-name">VELM BUILD</p>

    <h1 class="slogan">
      <span class="slogan-line slogan-line--strong">DON'T MOVE,</span>
      <span class="slogan-line slogan-line--light">RE-IMAGINE</span>
    </h1>

    <ul class="services">
      <li class="service">NEW HOMES</li>
      <li class="service service--dark">RENNOVATIONS</li>
      <li class="service">ADDITIONS</li>
    </ul>

    <p class="website">www.velmbuild.com.au</p>
  </section>
</body>
</html>
```